Anzeigengestaltung für Dienstleister für die professionelle Planung und Beschaffung von IT-Lösungen
Zielgruppe
Wir sind Dienstleister für die professionelle Planung und Beschaffung von IT-Lösungen.
Wir bieten umfassende und umfangreiche sowie produktneutrale Beratung zur Umsetzung Ihrer Digitalisierungsprojekte.
Unser Ziel ist es, Ihre individuellen Wünsche und Anforderungen mit speziell auf Sie abgestimmten Konzepten zu realisieren. Hierbei verstehen wir uns als Teamplayer, der alle Aspekte der verschiedenen Fachbereiche zu kombinieren versteht.
Fokus:
Neben den technischen Lösungen erarbeiten wir die detaillierten Anforderungen für Vergabeverfahren (öffentliche Ausschreibung national und EU weit)
Beratung
Planung
Erarbeiten von professionellen und produktneutralen Ausschreibungsunterlagen
Durchführen der Ausschreibung und Vergabe
Professionelle Dokumentation
Professionelle Projektbegleitung bis zur Abnahme und Abrechnung
Bereiche:
Digitalisierung Schulen
Rechenzentren
Telefon Lösungen
Druck Lösungen
Netzwerk und WLAN Lösungen
Zielkunden:
Öffentliche Kunde wie z.B. Kommunen, Schulen, Rathäuser, Hochschulen
Aufgabenstellung
OnePager A4 als Werbeflyer zur Darstellung meines Unternehmen, Neukundengewinnung

```html
<!DOCTYPE html>
<html lang="de">
<head>
<meta charset="utf-8">
<title>Datenbau – Die Zukunft ist digital!</title>
<link href="https://fonts.googleapis.com/css2?family=Open+Sans:wght@300;400&display=swap" rel="stylesheet">
<style>
  :root {
    --green: #93c01f;
    --graphite: #555555;
    --navy: #1d1a4a;
    --ink: #222222;
    --white: #ffffff;
  }
  * { margin: 0; padding: 0; box-sizing: border-box; }
  html, body { width: 848px; height: 1200px; overflow: hidden; background: var(--white); }
  body { font-family: "Open Sans", Arial, sans-serif; font-weight: 300; color: var(--ink); }
  .flyer { position: relative; width: 848px; height: 1200px; background: var(--white); overflow: hidden; }

  .hero-photo {
    position: absolute; left: 0; top: 0; width: 848px; height: 433px;
    background:
      radial-gradient(ellipse 70px 40px at 740px 250px, rgba(255,140,110,0.75) 0%, rgba(255,140,110,0) 100%),
      radial-gradient(ellipse 120px 90px at 505px 230px, rgba(222,180,150,0.85) 0%, rgba(200,150,120,0.45) 55%, rgba(200,150,120,0) 100%),
      radial-gradient(ellipse 150px 70px at 520px 400px, rgba(40,36,38,0.9) 0%, rgba(40,36,38,0) 100%),
      radial-gradient(ellipse 40px 160px at 220px 90px, rgba(225,235,220,0.55) 0%, rgba(225,235,220,0) 100%),
      radial-gradient(ellipse 60px 30px at 210px 255px, rgba(230,238,235,0.6) 0%, rgba(230,238,235,0) 100%),
      radial-gradient(ellipse 60px 30px at 90px 255px, rgba(200,215,220,0.45) 0%, rgba(200,215,220,0) 100%),
      radial-gradient(ellipse 55px 30px at 360px 250px, rgba(210,225,230,0.5) 0%, rgba(210,225,230,0) 100%),
      radial-gradient(ellipse 110px 200px at 820px 180px, rgba(190,95,45,0.85) 0%, rgba(190,95,45,0) 100%),
      linear-gradient(180deg, rgba(20,30,38,0) 50%, rgba(20,30,38,0.55) 100%),
      linear-gradient(90deg, #27404d 0%, #4e6a78 30%, #5a7480 50%, #4e5a60 72%, #7a5644 90%, #a5582f 100%);
  }

  .headline-band {
    position: absolute; left: 0; top: 433px; width: 443px; height: 80px;
    background: var(--green);
  }
  .headline-band h1 {
    position: absolute; left: 87px; top: 17px;
    font-weight: 300; font-size: 32px; color: var(--white); letter-spacing: 0.1px;
    white-space: nowrap;
  }

  .intro-box {
    position: absolute; left: 0; top: 524px; width: 444px; height: 344px;
    background: var(--graphite);
  }
  .intro-box p {
    position: absolute; left: 87px; top: 19px; width: 327px;
    font-size: 18px; line-height: 28.5px; color: var(--white);
    text-align: justify; hyphens: manual;
  }

  .brand {
    position: absolute; left: 494px; top: 452px; height: 50px;
    display: flex; align-items: center; gap: 10px;
  }
  .brand-dot { width: 22px; height: 22px; border-radius: 50%; background: var(--green); }
  .brand-name { font-size: 34px; font-weight: 300; color: var(--ink); letter-spacing: 1.5px; }
  .brand-rule {
    position: absolute; left: 748px; top: 506px; width: 26px; height: 1px;
    background: var(--green);
  }
  .services {
    position: absolute; left: 476px; top: 524px; width: 334px;
    display: flex; justify-content: space-between;
    font-size: 11.6px; font-weight: 400; letter-spacing: 0.4px; color: var(--ink);
  }

  .cta {
    position: absolute; left: 86px; top: 887px;
    font-size: 31px; font-weight: 300; color: var(--navy); white-space: nowrap;
  }

  .imprint {
    position: absolute; top: 1092px; font-style: normal;
    font-size: 10.4px; line-height: 16px; font-weight: 400; color: var(--ink);
  }
  .imprint-company { left: 96px; }
  .imprint-contact { left: 204px; }

  .web-address {
    position: absolute; left: 456px; top: 1088px;
    font-size: 29px; font-weight: 300; color: var(--green);
  }
  .footer-bar {
    position: absolute; left: 453px; top: 1145px; width: 395px; height: 55px;
    background: var(--graphite);
  }
</style>
</head>
<body>
<main class="flyer">
  <div class="hero-photo" role="img" aria-label="Fotografie: Geschäftsfrau in einer unscharfen Halle, überlagert von einem leuchtenden digitalen Netzwerk"></div>

  <section class="headline-band">
    <h1>Die Zukunft ist digital!</h1>
  </section>

  <section class="intro-box">
    <p>Unser Ziel ist es, Ihre individuellen Wün&shy;sche und Anforderungen mit speziell auf Sie abgestimmten Konzepten zu realisieren. Hierbei verstehen wir uns als Teamplayer, der alle Aspekte der ver&shy;schiedenen Fachbereiche zu kombinieren versteht. Neben den technischen Lösungen erarbeiten wir die detaillier&shy;ten Anforderungen für Ihr Vergabeverfahren.</p>
  </section>

  <div class="brand">
    <span class="brand-dot"></span>
    <span class="brand-name">DATENBAU</span>
  </div>
  <div class="brand-rule"></div>
  <nav class="services">
    <span>BERATUNG</span><span>PLANUNG</span><span>DURCHFÜHRUNG</span><span>BEGLEITUNG</span>
  </nav>

  <h2 class="cta">Verbinde Dich mit uns!</h2>

  <address class="imprint imprint-company">
    Datenbau GmbH<br>Lindenweg 14<br>88299 Musterfeld
  </address>
  <address class="imprint imprint-contact">
    GF: Lukas Brenner<br>Tel: 07500 / 123456-0<br>&nbsp;info@datenbau-it.de
  </address>

  <div class="web-address">datenbau-it.de</div>
  <div class="footer-bar"></div>
</main>
</body>
</html>
```